New Advertising Company Business Card

A two sided business card. One side with logo only and the other side with my information and maybe my logo again. Looking for something unique and creative, but not too busy. Info would include my name(Marcus Feldon), President, phone number, address, email address, and website. LOGO IS THE BLUE AND WHITE ONE.

Target Market(s)

CEO/VP Level Audience

Industry/Entity Type

Business

Contact Information for Business Card

In Description.

```html
<!DOCTYPE html>
<html lang="en">
<head>
<meta charset="UTF-8">
<title>Arcline Media Business Card</title>
<link href="https://fonts.googleapis.com/css2?family=Open+Sans:wght@400;600;700&display=swap" rel="stylesheet">
<style>
  :root {
    --backdrop: #1e2023;
    --card-dark: #2a2a2b;
    --card-dark-mark: #3b3b3d;
    --card-light-top: #ffffff;
    --card-light-bottom: #d4d4d6;
    --ink: #1c1c1e;
    --brand-blue: #1466ad;
  }
  * { margin: 0; padding: 0; box-sizing: border-box; }
  html, body {
    width: 1200px;
    height: 900px;
    overflow: hidden;
    background: var(--backdrop);
    font-family: "Open Sans", sans-serif;
  }
  .canvas {
    position: relative;
    width: 1200px;
    height: 900px;
  }
  .card {
    position: absolute;
    left: 250px;
    width: 700px;
    height: 400px;
    overflow: hidden;
    box-shadow: 0 10px 30px rgba(0,0,0,0.45);
  }
  .card-back {
    top: 40px;
    background: var(--card-dark);
    display: flex;
    align-items: center;
    justify-content: center;
  }
  .card-back .wordmark {
    color: var(--card-dark-mark);
    font-weight: 600;
    font-size: 46px;
    letter-spacing: 6px;
  }
  .card-front {
    top: 460px;
    background: linear-gradient(180deg, var(--card-light-top) 0%, var(--card-light-bottom) 100%);
  }
  .accent-arc {
    position: absolute;
    inset: 0;
    width: 700px;
    height: 400px;
  }
  .front-wordmark {
    position: absolute;
    left: 48px;
    top: 56px;
    color: var(--ink);
    font-weight: 600;
    font-size: 36px;
    letter-spacing: 4px;
    line-height: 1;
  }
  .address {
    position: absolute;
    left: 50px;
    top: 160px;
    color: var(--ink);
    font-size: 17px;
    line-height: 26px;
  }
  .contact-list {
    position: absolute;
    left: 50px;
    top: 232px;
    list-style: none;
    color: var(--ink);
    font-size: 17px;
    line-height: 28px;
  }
  .contact-list li {
    display: flex;
    align-items: center;
    gap: 10px;
  }
  .contact-list svg {
    width: 14px;
    height: 14px;
    flex: none;
  }
  .holder {
    position: absolute;
    right: 48px;
    top: 250px;
    text-align: right;
  }
  .holder-name {
    color: var(--brand-blue);
    font-weight: 700;
    font-size: 24px;
    line-height: 1.2;
  }
  .holder-title {
    color: var(--ink);
    font-size: 18px;
  }
</style>
</head>
<body>
<div class="canvas">
  <section class="card card-back">
    <div class="wordmark">ARCLINE MEDIA</div>
  </section>

  <section class="card card-front">
    <svg class="accent-arc" viewBox="0 0 700 400" aria-hidden="true">
      <path d="M355,420 C410,200 520,35 615,32 C655,31 688,65 712,112" fill="none" stroke="var(--brand-blue)" stroke-width="62"/>
    </svg>

    <div class="front-wordmark">ARCLINE MEDIA</div>

    <p class="address">42 Harbor Lane, Westfield Road<br>Crestview, CA 90412</p>

    <ul class="contact-list">
      <li>
        <svg viewBox="0 0 24 24"><path fill="var(--brand-blue)" d="M6.6 10.8a15.1 15.1 0 0 0 6.6 6.6l2.2-2.2a1 1 0 0 1 1-.25 11.4 11.4 0 0 0 3.6.57 1 1 0 0 1 1 1V20a1 1 0 0 1-1 1A17 17 0 0 1 3 4a1 1 0 0 1 1-1h3.5a1 1 0 0 1 1 1c0 1.25.2 2.45.57 3.6a1 1 0 0 1-.25 1z"/></svg>
        +1 310 555 0147
      </li>
      <li>
        <svg viewBox="0 0 24 24"><rect x="2" y="5" width="20" height="14" rx="2" fill="var(--brand-blue)"/><path d="M3 6l9 7 9-7" stroke="#fff" stroke-width="1.8" fill="none"/></svg>
        hello@arclinemedia.com
      </li>
      <li>
        <svg viewBox="0 0 24 24"><circle cx="12" cy="12" r="9.5" fill="none" stroke="var(--brand-blue)" stroke-width="2"/><path d="M2.5 12h19M12 2.5c3 3 3 16 0 19M12 2.5c-3 3-3 16 0 19" fill="none" stroke="var(--brand-blue)" stroke-width="1.6"/></svg>
        www.arclinemedia.com
      </li>
    </ul>

    <div class="holder">
      <div class="holder-name">Marcus Feldon</div>
      <div class="holder-title">President</div>
    </div>
  </section>
</div>
</body>
</html>
```